디자인 카테고리
모바일 앱 (IT/미디어 업종)
브랜드 소개
TOLU은 "Turn Over Leaves Upward"의 약자로, 블록코딩에서 텍스트코딩으로 이어주는 징검다리 역할을 해주고자 하는 서비스입니다. 블록코딩으로 문제를 풀어나가며 문제점을 해결하고, 텍스트 언어와의 변환을 통해 텍스트 코드 또한 배울 수 있는 문제풀이 App입니다.

```html
<!DOCTYPE html>
<html lang="ko">
<head>
<meta charset="utf-8">
<title>TOLU 어플리케이션 – 화면 디자인</title>
<link rel="stylesheet" href="https://fonts.googleapis.com/css2?family=Noto+Sans+KR:wght@400;500;700&family=Poppins:wght@500;700&display=swap">
<style>
  :root{
    --bg:#f4f6fb;
    --card:#ffffff;
    --blue:#4f8ef7;
    --sky:#6fa3f8;
    --violet:#a977f2;
    --lavender:#c9aaf6;
    --orange:#f5b445;
    --ink:#3a3f58;
    --muted:#9aa0b5;
    --line:#e6e9f2;
    --grad:linear-gradient(160deg,var(--sky) 0%,var(--violet) 100%);
  }
  *{box-sizing:border-box;margin:0;padding:0}
  html,body{width:1200px;height:1200px;overflow:hidden}
  body{background:var(--bg);font-family:"Noto Sans KR",sans-serif;color:var(--ink);position:relative}

  .brand{position:absolute;left:85px;top:80px;display:flex;align-items:center;gap:22px}
  .brand-square{width:96px;height:96px;border-radius:14px;background:var(--grad)}
  .brand-name{font-family:"Poppins",sans-serif;font-weight:700;font-size:52px;letter-spacing:2px;color:var(--violet);line-height:1}
  .brand-tagline{font-family:"Poppins",sans-serif;font-weight:500;font-size:15px;color:var(--violet);margin-top:6px}

  .row{position:absolute;left:0;width:1200px;display:flex;justify-content:center;gap:50px}
  .row-top{top:250px}
  .row-bottom{top:700px}

  .screen{width:220px;height:400px;border-radius:22px;background:var(--card);box-shadow:0 14px 34px rgba(79,110,200,.16);overflow:hidden;position:relative;display:flex;flex-direction:column}
  .status{height:22px;font-size:9px;display:flex;align-items:center;justify-content:center;color:var(--muted)}
  .status.light{color:#fff}

  /* splash */
  .splash{background:var(--grad);align-items:center;justify-content:center}
  .splash .status{position:absolute;top:0;left:0;right:0}
  .splash-name{font-family:"Poppins",sans-serif;font-weight:700;font-size:34px;color:#fff;letter-spacing:2px}
  .dots{display:flex;gap:5px;justify-content:center;margin-top:12px}
  .dots i{width:6px;height:6px;border-radius:50%;background:var(--line)}
  .dots i.on{background:var(--blue)}
  .splash .dots i{background:rgba(255,255,255,.5)}
  .splash .dots i.on{background:#fff}
  .splash-foot{position:absolute;bottom:22px;font-family:"Poppins",sans-serif;font-weight:700;font-size:12px;color:#fff}

  /* onboarding */
  .onboard{padding:0 20px 22px}
  .onboard-title{font-size:20px;font-weight:700;margin-top:18px}
  .onboard-sub{font-size:10px;color:var(--muted);margin-top:4px}
  .onboard-art{flex:1;display:flex;align-items:center;justify-content:center}
  .art-fill{width:150px;height:130px;border-radius:10px;background:linear-gradient(135deg,var(--blue),var(--lavender))}
  .btn{height:38px;border-radius:19px;background:var(--grad);color:#fff;font-size:12px;font-weight:500;display:flex;align-items:center;justify-content:center;margin-top:14px}

  /* hero */
  .hero{background:linear-gradient(180deg,#eef1ff 0%,#d9ccfb 100%);align-items:center}
  .hero-name{font-family:"Poppins",sans-serif;font-weight:700;font-size:28px;color:var(--violet);margin-top:28px;letter-spacing:1px}
  .hero-tag{font-family:"Poppins",sans-serif;font-size:8px;color:var(--violet)}
  .hero-art{margin-top:26px;width:180px;height:220px;border-radius:14px;background:linear-gradient(150deg,var(--lavender) 0%,var(--violet) 55%,var(--blue) 100%)}

  /* profile */
  .profile{padding:0 16px}
  .profile-head{display:flex;align-items:center;gap:10px;margin-top:6px}
  .avatar{width:36px;height:36px;border-radius:50%;background:var(--lavender)}
  .profile-name{font-size:13px;font-weight:700;color:var(--blue)}
  .profile-level{font-size:9px;color:var(--muted)}
  .radar{display:block;margin:8px auto 4px}
  .stat{display:flex;align-items:center;gap:8px;font-size:9px;padding:6px 0;border-top:1px solid var(--line)}
  .stat-label{width:48px}
  .stat-bar{flex:1;height:5px;border-radius:3px;background:var(--line);position:relative}
  .stat-bar span{position:absolute;left:0;top:0;bottom:0;border-radius:3px;background:var(--grad)}
  .stat-value{width:24px;text-align:right;color:var(--muted)}
  .tabbar{position:absolute;left:0;right:0;bottom:0;height:40px;border-top:1px solid var(--line);display:flex;justify-content:space-around;align-items:center}
  .tab{width:14px;height:14px;border-radius:4px;border:2px solid var(--muted)}
  .tab.on{border-color:var(--blue);background:var(--blue);border-radius:50%;width:22px;height:22px}

  /* forms */
  .form-top{height:110px;background:var(--grad);display:flex;flex-direction:column;align-items:center}
  .form-top .name{font-family:"Poppins",sans-serif;font-weight:700;font-size:24px;color:#fff;margin-top:24px}
  .form-card{margin:-40px 14px 0;background:#fff;border-radius:12px;box-shadow:0 6px 18px rgba(79,110,200,.14);padding:14px}
  .form-title{font-size:14px;font-weight:700;text-align:center;color:var(--blue)}
  .form-sub{font-size:8px;text-align:center;color:var(--muted);margin-bottom:8px}
  .field{display:flex;align-items:center;gap:6px;border-bottom:1px solid var(--line);padding:8px 0;font-size:9px}
  .field-label{width:46px;color:var(--muted)}
  .field-value{flex:1}
  .tag{font-size:8px;color:#fff;background:var(--orange);border-radius:8px;padding:2px 7px}
  .form-actions{padding:0 14px}
  .form-links{font-size:8px;color:var(--muted);text-align:center;margin-top:8px}
</style>
</head>
<body>

<header class="brand">
  <div class="brand-square"></div>
  <div>
    <div class="brand-name">TOLU</div>
    <div class="brand-tagline">Turn Over Leaves Upward</div>
  </div>
</header>

<section class="row row-top">
  <article class="screen splash">
    <div class="status light">9:41</div>
    <div class="splash-name">TOLU</div>
    <div class="dots"><i class="on"></i><i></i><i></i></div>
    <div class="splash-foot">TOLU</div>
  </article>

  <article class="screen profile">
    <div class="status">9:41</div>
    <div class="profile-head">
      <div class="avatar"></div>
      <div>
        <div class="profile-name">Min Seo</div>
        <div class="profile-level">Lv.3 코더</div>
      </div>
    </div>
    <svg class="radar" width="150" height="130" viewBox="0 0 150 130">
      <polygon points="75,8 140,50 115,122 35,122 10,50" fill="none" stroke="#e6e9f2"/>
      <polygon points="75,36 112,56 98,102 52,102 38,56" fill="none" stroke="#e6e9f2"/>
      <polygon points="75,18 128,54 92,108 45,96 30,56" fill="#a977f2" fill-opacity=".55" stroke="#4f8ef7" stroke-width="1.5"/>
    </svg>
    <div class="stat"><span class="stat-label">정답률</span><div class="stat-bar"><span style="width:82%"></span></div><span class="stat-value">82%</span></div>
    <div class="stat"><span class="stat-label">풀이 수</span><div class="stat-bar"><span style="width:60%"></span></div><span class="stat-value">46</span></div>
    <div class="stat"><span class="stat-label">연속 학습</span><div class="stat-bar"><span style="width:40%"></span></div><span class="stat-value">7일</span></div>
    <nav class="tabbar"><i class="tab"></i><i class="tab"></i><i class="tab on"></i><i class="tab"></i><i class="tab"></i></nav>
  </article>

  <article class="screen hero">
    <div class="status">9:41</div>
    <div class="hero-name">TOLU</div>
    <div class="hero-tag">Turn Over Leaves Upward</div>
    <div class="hero-art" role="img" aria-label="보라색과 파란색 입체 블록이 떠 있는 일러스트"></div>
  </article>

  <article class="screen onboard">
    <div class="status">9:41</div>
    <div class="onboard-title">피드백</div>
    <div class="onboard-sub">풀이 결과로 약점을 찾아요</div>
    <div class="onboard-art">
      <svg width="160" height="130" viewBox="0 0 160 130">
        <line x1="10" y1="120" x2="150" y2="120" stroke="#3a3f58" stroke-width="2"/>
        <rect x="22" y="80" width="18" height="40" fill="#c9aaf6"/>
        <rect x="50" y="62" width="18" height="58" fill="#4f8ef7"/>
        <rect x="78" y="70" width="18" height="50" fill="#a977f2"/>
        <rect x="106" y="44" width="18" height="76" fill="#4f8ef7"/>
        <polyline points="20,76 58,50 86,60 136,22" fill="none" stroke="#3a3f58" stroke-width="2"/>
        <polyline points="126,20 138,21 136,33" fill="none" stroke="#3a3f58" stroke-width="2"/>
      </svg>
    </div>
    <div class="dots"><i class="on"></i><i></i><i></i></div>
    <div class="btn">시작하기</div>
  </article>
</section>

<section class="row row-bottom">
  <article class="screen">
    <div class="status light" style="position:absolute;top:0;left:0;right:0">9:41</div>
    <div class="form-top"><div class="name">TOLU</div></div>
    <div class="form-card">
      <div class="form-title">회원가입</div>
      <div class="form-sub">Sign up to TOLU</div>
      <div class="field"><span class="field-label">아이디</span><span class="field-value">tolu_user</span><span class="tag">확인</span></div>
      <div class="field"><span class="field-label">비밀번호</span><span class="field-value">••••••</span></div>
      <div class="field"><span class="field-label">이메일</span><span class="field-value">user@mail.kr</span><span class="tag">확인</span></div>
      <div class="field"><span class="field-label">생년월일</span><span class="field-value">2005.03.14</span></div>
    </div>
    <div class="form-actions"><div class="btn">가입하기</div></div>
  </article>

  <article class="screen">
    <div class="status light" style="position:absolute;top:0;left:0;right:0">9:41</div>
    <div class="form-top" style="height:170px"><div class="name" style="margin-top:44px">TOLU</div></div>
    <div class="form-card">
      <div class="field"><span class="field-label">아이디</span><span class="field-value">tolu_user</span></div>
      <div class="field"><span class="field-label">비밀번호</span><span class="field-value">••••••</span></div>
    </div>
    <div class="form-actions">
      <div class="btn">로그인</div>
      <div class="form-links">비밀번호 찾기 | 회원가입</div>
    </div>
  </article>

  <article class="screen onboard">
    <div class="status">9:41</div>
    <div class="onboard-title">학습</div>
    <div class="onboard-sub">블록을 텍스트 코드로 바꿔봐요</div>
    <div class="onboard-art">
      <div class="art-fill" role="img" aria-label="코드 블록 위에 돋보기를 올려 둔 일러스트"></div>
    </div>
    <div class="dots"><i></i><i class="on"></i><i></i></div>
    <div class="btn">다음</div>
  </article>
</section>

</body>
</html>
```